Website design for legal tech start up in Switzerland (B2B)

We are for a legal tech start up in Switzerland called TAVO. We have been running since August 2016. This will be our first live website.

We need a website designed and business card design for our start-up in Switzerland. We also need the Web design to be converted into HTML and CSS files.

Function of website:
• To inform potential customers of our services
• Form a key part of our digital marketing and sales footprint.
• Branding

Please find attached logo.
Updates

Project Deadline Extended Reason: Giving us time to review submissions and provide opportunity for more submissions. Added Thursday, February 16, 2017

Reason: Looking for more idea's not necessarily set on blue and grey colours only.

Target Market(s)

B2B tech powered legal services.

Industry/Entity Type

Legal

Contact Information for Business Card

Lean and slick design.

Coding

Coded - Design and coding required

Number of Pages Required

5+ page

Requirements
Must have
• VERY LEAN AND CLEAN DESIGN!
• We have received many great standard designs, but we are looking for something more out-of-the box: You can get inspiration from these designs: http://www.pindelsite.com/websites/clean/
• Thanks!!
• Easy content management system
• Well structured coding for additional development
• Responsive webpage for all types of devices
• SEO optimized
• Tabs (Home, services, team, careers, blog, contact us)
• Colour scheme complementary to logo
Nice to have
• Look and Design - Approachable, High-tech, Modern
• Easy to add chat bot capability in future
Should not have
• Too busy/ too much clutter
• Not take to long to load

```html
<!DOCTYPE html>
<html lang="en">
<head>
<meta charset="utf-8">
<title>TAVO – Legal Tech Start Up in Switzerland</title>
<link href="https://fonts.googleapis.com/css2?family=Oswald:wght@400;500;700&family=Open+Sans:wght@400;600;700&display=swap" rel="stylesheet">
<style>
:root{
  --navy:#0e2553;
  --navy-deep:#0a1a3d;
  --blue:#1c4a9c;
  --blue-mid:#2a5cb4;
  --yellow:#f3bf1b;
  --ink:#2b2f38;
  --grey:#6b7280;
  --light:#eef1f6;
  --white:#ffffff;
}
*{box-sizing:border-box;margin:0;padding:0}
html,body{width:1200px;height:3860px;overflow:hidden}
body{font-family:"Open Sans",Arial,sans-serif;color:var(--ink);background:var(--white);font-size:13px;line-height:1.5}
h1,h2,h3,h4,.btn,.nav a{font-family:"Oswald","Arial Narrow",sans-serif}
section,header,footer{position:relative;width:1200px;overflow:hidden}
.photo{position:absolute;inset:0}
.btn{display:inline-block;background:var(--yellow);color:var(--navy);font-weight:500;font-size:13px;letter-spacing:.5px;padding:8px 22px;text-transform:uppercase}

/* header */
.site-header{height:72px;background:var(--white);display:flex;align-items:center;padding:0 40px 0 60px;box-shadow:0 2px 6px rgba(0,0,0,.15);z-index:2}
.logo{display:flex;align-items:center;gap:10px;font-family:"Oswald",sans-serif;font-weight:700;font-size:38px;color:var(--navy);letter-spacing:2px}
.logo i{width:14px;height:14px;background:var(--blue)}
.header-right{margin-left:auto;text-align:right}
.contact-line{font-size:11px;color:var(--grey);margin-bottom:8px}
.contact-line span{margin-left:18px}
.nav a{font-size:13px;color:var(--navy);text-decoration:none;margin-left:26px;text-transform:uppercase;letter-spacing:.5px}
.nav a.active{color:var(--blue-mid);border-bottom:2px solid var(--yellow)}

/* hero */
.hero{height:528px;color:var(--white);text-align:center}
.hero .photo{background:linear-gradient(180deg,#5c6672 0%,#3a4656 45%,#1a2c55 100%)}
.hero .shade{position:absolute;inset:0;background:linear-gradient(180deg,rgba(14,37,83,0) 40%,rgba(14,37,83,.85) 100%)}
.hero-text{position:absolute;left:0;right:0;top:320px}
.hero h1{font-size:50px;line-height:1.05;font-weight:700;letter-spacing:1px;text-transform:uppercase;text-shadow:0 2px 8px rgba(0,0,0,.4)}
.hero .tagline{font-family:"Oswald",sans-serif;color:var(--yellow);font-size:26px;letter-spacing:1px;text-transform:uppercase;margin-top:6px}

/* promise band */
.promise{height:80px;background:var(--blue);color:var(--white);text-align:center;padding-top:16px}
.promise h2{font-size:22px;font-weight:500;letter-spacing:1px;text-transform:uppercase}
.promise ul{list-style:none;display:flex;justify-content:center;gap:40px;font-size:11px;margin-top:4px;text-transform:uppercase}
.promise li::before{content:"✓ ";color:var(--yellow)}

/* jobs */
.jobs{height:460px}
.jobs .photo{background:linear-gradient(135deg,#1f3a6e,#0d2148 60%,#14305f)}
.jobs-panel{position:absolute;left:240px;top:40px;width:720px;height:390px;background:rgba(10,26,61,.82);padding:28px 24px;color:var(--white)}
.jobs h2{font-size:28px;text-transform:uppercase;font-weight:500;letter-spacing:1px}
.search-row{display:flex;gap:10px;margin:14px 0 30px}
.search-row .field{flex:1;height:32px;background:var(--white);color:var(--grey);font-size:11px;padding:8px 10px}
.sectors{display:grid;grid-template-columns:220px 1fr 1fr;gap:20px}
.sectors h3{font-size:26px;text-transform:uppercase;line-height:1.1;font-weight:500;margin-bottom:8px}
.sectors h4{font-size:13px;color:var(--white);margin-bottom:4px}
.sectors ul{list-style:none;font-size:12px;color:var(--yellow);line-height:1.55}

/* welcome */
.welcome{height:500px}
.welcome .photo{background:linear-gradient(90deg,#c9ced6,#8e98a8 45%,#5a6a84)}
.welcome-panel{position:absolute;left:240px;top:40px;width:720px;height:420px;background:var(--white);box-shadow:0 4px 18px rgba(0,0,0,.25)}
.welcome-panel h2{background:var(--navy);color:var(--white);font-size:26px;font-weight:500;text-transform:uppercase;padding:16px 24px;letter-spacing:1px}
.welcome-body{display:flex;gap:22px;padding:20px 24px}
.welcome-body p{font-size:11.5px;color:var(--grey);margin-bottom:10px}
.welcome-photo{flex:0 0 230px;height:230px;background:linear-gradient(160deg,#dfe3ea,#a8b3c4)}
.welcome-panel .readmore{position:absolute;bottom:0;left:0;right:0;background:var(--navy);color:var(--white);text-align:center;font-family:"Oswald",sans-serif;font-size:12px;padding:8px;text-transform:uppercase}

/* services */
.services{height:650px;background:var(--white)}
.services-wrap{position:absolute;left:240px;top:40px;width:720px}
.services-top{display:flex;gap:24px}
.services-intro{flex:0 0 330px;background:var(--light);padding:20px;border-left:4px solid var(--blue)}
.services-intro h2{font-size:24px;color:var(--blue);text-transform:uppercase;font-weight:500}
.services-intro p{font-size:12.5px;color:var(--ink)}
.services-title{font-family:"Oswald",sans-serif;font-weight:700;font-size:58px;line-height:1;color:var(--navy);text-transform:uppercase;padding-top:6px}
.service-cards{display:grid;grid-template-columns:repeat(3,1fr);gap:14px;margin-top:24px}
.service-card{background:var(--blue);color:var(--white)}
.service-card .thumb{height:130px;background:linear-gradient(160deg,#c5ccd8,#7d8ba3)}
.service-card h3{font-size:20px;text-transform:uppercase;font-weight:500;padding:10px 12px 4px;background:var(--navy)}
.service-card p{font-size:11px;padding:10px 12px;color:#dbe4f5}
.service-card .btn{margin:0 12px 14px;font-size:11px;padding:6px 14px}

/* blog */
.blog{height:510px}
.blog .photo{background:linear-gradient(135deg,#2a3a55,#121e36 55%,#23375c)}
.blog-panel{position:absolute;left:240px;top:40px;width:720px;height:430px;background:rgba(255,255,255,.96)}
.blog-panel h2{background:var(--navy);color:var(--white);font-size:26px;font-weight:500;text-transform:uppercase;padding:14px 24px}
.posts{display:grid;grid-template-columns:1.4fr 1fr 1fr;gap:12px;padding:14px}
.post .thumb{height:150px;background:linear-gradient(160deg,#d0d5de,#8894aa);position:relative}
.post .date{position:absolute;left:0;top:0;background:var(--navy);color:var(--white);font-size:10px;padding:3px 8px;text-transform:uppercase}
.post h3{font-family:"Open Sans",sans-serif;font-size:13px;font-weight:700;color:var(--navy);margin:8px 0 4px}
.post p{font-size:11px;color:var(--grey)}
.blog-panel .readmore{position:absolute;bottom:0;left:0;right:0;background:var(--navy);color:var(--white);text-align:center;font-family:"Oswald",sans-serif;font-size:12px;padding:8px;text-transform:uppercase}

/* team */
.team{height:400px;background:linear-gradient(180deg,var(--blue) 0%,var(--navy) 100%);text-align:center;color:var(--white);padding-top:40px}
.team h2{font-size:30px;font-weight:500;text-transform:uppercase;letter-spacing:1px}
.members{display:flex;justify-content:center;gap:60px;margin:30px 0 26px}
.member .avatar{width:110px;height:110px;border-radius:50%;border:4px solid var(--white);background:linear-gradient(160deg,#c9cfd9,#7f8ca4);margin:0 auto 10px}
.member h4{font-size:14px;font-weight:500;text-transform:uppercase}
.member span{font-size:11px;color:#c7d4ee}

/* testimonial */
.testimonial{height:240px;text-align:center;color:var(--white)}
.testimonial .photo{background:linear-gradient(135deg,#2b3344,#141b2b 60%,#263145)}
.testimonial-body{position:absolute;left:0;right:0;top:0}
.testimonial .avatar{width:96px;height:96px;border-radius:50%;border:4px solid var(--white);background:linear-gradient(160deg,#c9cfd9,#7f8ca4);margin:-10px auto 8px}
.testimonial h4{font-size:18px;font-weight:500;text-transform:uppercase}
.testimonial .role{font-size:11px;color:var(--yellow)}
.testimonial p{width:780px;margin:10px auto 0;font-size:12px;color:#d6dbe6}
.dots{margin-top:10px}
.dots i{display:inline-block;width:8px;height:8px;border-radius:50%;background:#778;margin:0 3px}
.dots i.on{background:var(--yellow)}

/* newsletter */
.newsletter{height:100px;background:var(--navy);display:flex;align-items:center;padding:0 240px;color:var(--white)}
.newsletter h2{font-size:24px;font-weight:500;text-transform:uppercase;letter-spacing:1px}
.newsletter .field{margin-left:auto;width:260px;height:32px;background:var(--white);color:var(--grey);font-size:11px;padding:8px 10px}
.newsletter .btn{margin-left:10px}

/* footer */
.site-footer{height:292px;background:var(--navy-deep);color:#b8c3d8;padding:40px 60px}
.footer-cols{display:grid;grid-template-columns:repeat(4,1fr);gap:40px}
.site-footer h4{font-family:"Oswald",sans-serif;color:var(--white);font-size:15px;font-weight:500;text-transform:uppercase;margin-bottom:12px;border-bottom:2px solid var(--yellow);display:inline-block;padding-bottom:3px}
.site-footer ul{list-style:none;font-size:11.5px;line-height:1.4}
.site-footer li{margin-bottom:8px}
.site-footer li small{display:block;color:#7f8aa3;font-size:10px}
.socials{display:flex;gap:8px;margin-top:12px}
.socials i{width:20px;height:20px;border-radius:50%;background:var(--blue)}
.copyright{height:28px;background:#07132e;color:#8893aa;font-size:10.5px;padding:6px 60px}
</style>
</head>
<body>

<header class="site-header">
  <div class="logo"><i></i>TAVO</div>
  <div class="header-right">
    <div class="contact-line"><span>+41 44 555 01 23</span><span>hello@tavo-legal.ch</span></div>
    <nav class="nav">
      <a class="active" href="#">Home</a><a href="#">Services</a><a href="#">Team</a><a href="#">Careers</a><a href="#">Blog</a><a href="#">Contact Us</a>
    </nav>
  </div>
</header>

<section class="hero">
  <div class="photo" role="img" aria-label="Photo of a smiling business team in a meeting"></div>
  <div class="shade"></div>
  <div class="hero-text">
    <h1>Digital Marketing<br>&amp; Sales Footprint<br>Legal Tech</h1>
    <div class="tagline">Legal Tech Start Up in Switzerland</div>
  </div>
</section>

<section class="promise">
  <h2>We solve online marketing problems with proven solutions.</h2>
  <ul><li>Swiss law</li><li>Lean legal</li><li>Proven services</li><li>Since 2016</li></ul>
</section>

<section class="jobs">
  <div class="photo" role="img" aria-label="Dark blue office photo background"></div>
  <div class="jobs-panel">
    <h2>Search Jobs</h2>
    <div class="search-row">
      <div class="field">Keywords</div><div class="field">Location</div><div class="field">Sector</div>
      <span class="btn">Search Now</span>
    </div>
    <div class="sectors">
      <div>
        <h3>Sector<br>Specialism</h3>
        <ul><li>Content Marketing</li><li>Search Engine Optimisation</li><li>Social Media Marketing</li><li>Influencer Marketing</li><li>Digital Advertising</li><li>Marketing Analytics</li><li>Conversion Optimisation</li></ul>
      </div>
      <div>
        <h3>Roles</h3>
        <h4>B2B</h4>
        <ul><li>Content Marketing</li><li>Search Engine Marketing</li><li>Social Media Manager</li><li>Influencer Relations</li><li>Digital Advertising</li><li>PPC &amp; Social Media</li><li>Email Marketing</li><li>Marketing Analytics</li></ul>
      </div>
      <div>
        <h3>&nbsp;</h3>
        <h4>B2C</h4>
        <ul><li>Content Marketing</li><li>Search Engine Marketing</li><li>Social Media Marketing</li><li>Influencer Marketing</li><li>Digital Advertising</li><li>Website Analytics</li><li>Conversion Optimisation</li></ul>
      </div>
    </div>
  </div>
</section>

<section class="welcome">
  <div class="photo" role="img" aria-label="Photo of business people working at a desk"></div>
  <div class="welcome-panel">
    <h2>Welcome to TAVO</h2>
    <div class="welcome-body">
      <div>
        <p>TAVO brings modern technology to legal work for Swiss companies. We combine experienced lawyers with smart software so that contracts, compliance and corporate matters are handled quickly, clearly and at a fair, predictable price for every client we serve.</p>
        <p>Since August 2016 we have helped start ups and growing businesses set up, scale and protect their ideas. Our team listens first, explains in plain language and delivers results you can rely on every day.</p>
        <p>Whether you need a single contract review or an ongoing legal partner, we adapt to your pace and keep your legal footprint lean and simple.</p>
      </div>
      <div class="welcome-photo" role="img" aria-label="Photo of a smiling businesswoman"></div>
    </div>
    <div class="readmore">Read More</div>
  </div>
</section>

<section class="services">
  <div class="services-wrap">
    <div class="services-top">
      <div class="services-intro">
        <h2>Marketing Services</h2>
        <p>Marketing services is the name we give to everything we do to help promote your online campaign. Whether you are looking at new content, offering a promotion, or launching a new product, website or service, we use digital marketing methods like social media channels, search engine marketing and pay per click advertising to achieve maximum exposure in front of the right audience.</p>
      </div>
      <div class="services-title">Digital<br>Marketing<br>Sales<br>Footprint</div>
    </div>
    <div class="service-cards">
      <div class="service-card">
        <div class="thumb" role="img" aria-label="Photo of a team discussing sales"></div>
        <h3>Sales Footprint</h3>
        <p>We map where your clients search and help you appear there with clear, trusted messages that turn visits into real enquiries.</p>
        <span class="btn">Read More</span>
      </div>
      <div class="service-card">
        <div class="thumb" role="img" aria-label="Photo of colleagues in a workshop"></div>
        <h3>Loop Marketing</h3>
        <p>Measure, learn and improve. Our loop approach keeps every campaign tested so your budget always works harder each month.</p>
        <span class="btn">Read More</span>
      </div>
      <div class="service-card">
        <div class="thumb" role="img" aria-label="Photo of a branding meeting"></div>
        <h3>Our Branding</h3>
        <p>A consistent voice and look across every channel builds trust. We shape branding that feels modern, approachable and clear.</p>
        <span class="btn">Read More</span>
      </div>
    </div>
  </div>
</section>

<section class="blog">
  <div class="photo" role="img" aria-label="Dark photo of a business meeting background"></div>
  <div class="blog-panel">
    <h2>From Our Blog</h2>
    <div class="posts">
      <div class="post">
        <div class="thumb" role="img" aria-label="Photo of a team at a laptop"><span class="date">August 16, 2017</span></div>
        <h3>How to Keep Up With Social Media News &amp; Trends</h3>
        <p>Short practical tips to follow changes in social platforms without losing focus on your own clients and daily work.</p>
      </div>
      <div class="post">
        <div class="thumb" role="img" aria-label="Photo of a presentation"><span class="date">August 16, 2017</span></div>
        <h3>Sales Consultants Your Guide to Online Success</h3>
        <p>What a good consultant brings and how to choose one that fits your stage.</p>
      </div>
      <div class="post">
        <div class="thumb" role="img" aria-label="Photo of colleagues reviewing documents"><span class="date">August 16, 2017</span></div>
        <h3>The Ultimate Guide to Search Engines in 2017</h3>
        <p>Key ranking changes every small legal business should know this year.</p>
      </div>
    </div>
    <div class="readmore">Read More</div>
  </div>
</section>

<section class="team">
  <h2>What Our Team Looks Like</h2>
  <div class="members">
    <div class="member"><div class="avatar" role="img" aria-label="Portrait of Jonas Brandt"></div><h4>Jonas Brandt</h4><span>Consultant Support</span></div>
    <div class="member"><div class="avatar" role="img" aria-label="Portrait of Alina Roth"></div><h4>Alina Roth</h4><span>Consultant Support</span></div>
    <div class="member"><div class="avatar" role="img" aria-label="Portrait of Bruno Pfister"></div><h4>Bruno Pfister</h4><span>Consultant Support</span></div>
    <div class="member"><div class="avatar" role="img" aria-label="Portrait of Rahel Bauer"></div><h4>Rahel Bauer</h4><span>Consultant Support</span></div>
  </div>
  <span class="btn">Meet Our Team</span>
</section>

<section class="testimonial">
  <div class="photo" role="img" aria-label="Dark photo of people in an office"></div>
  <div class="testimonial-body">
    <div class="avatar" role="img" aria-label="Portrait of Remo Portmann"></div>
    <h4>Remo Portmann</h4>
    <div class="role">Project Manager</div>
    <p>Working with TAVO changed how we handle legal questions. Answers come fast, costs are clear and the team always explains things in a way our whole company understands. We can focus on growth again.</p>
    <div class="dots"><i class="on"></i><i></i><i></i></div>
  </div>
</section>

<section class="newsletter">
  <h2>Sign Up for Newsletter</h2>
  <div class="field">Email Address</div>
  <span class="btn">Sign Up Now</span>
</section>

<footer class="site-footer">
  <div class="footer-cols">
    <div><h4>Recent Post</h4><ul><li>Keeping Legal Work Lean<small>12 May 2017</small></li><li>Keeping Legal Work Lean<small>12 May 2017</small></li><li>Keeping Legal Work Lean<small>12 May 2017</small></li></ul></div>
    <div><h4>Recent Comments</h4><ul><li>Great read for founders<small>by Anna</small></li><li>Great read for founders<small>by Marco</small></li><li>Great read for founders<small>by Lea</small></li></ul></div>
    <div><h4>Archives</h4><ul><li>March 2017</li><li>February 2017</li><li>January 2017</li><li>December 2016</li></ul></div>
    <div><h4>About TAVO</h4><ul><li>Tech powered legal services for Swiss businesses since 2016. Lean, clear and built around you.</li><li>hello@tavo-legal.ch<br>+41 44 555 01 23</li></ul><div class="socials"><i></i><i></i><i></i><i></i></div></div>
  </div>
</footer>
<div class="copyright">Copyright © 2017 TAVO. All Rights Reserved.</div>

</body>
</html>
```